Business cards and stationary for seafood company in Iceland
From Calm and Lofty Fjordland
Business cards and stationary for seafood company in Iceland - Food
Creative Brief
Simple
VEXA-Fjord ehf.
President
Hvalsteinsgata 17 108 Reykjavik Iceland
tmelvar58@brindlemail.com
Use all your creative words to express my new logo which just got from this website.
korvadesigns korvadesigns
vexafjord vexafjord
#114 is perfect! thanks a lot!
I couldn't find AI or EPS format from the files I downloaded from your web. I need help on that! Thanks.
Oh, Sorry, I am getting the LOGO now on this web. I don't know I should get the logo first and then ask for card design later. It seemed that I made a mistake by launch this too early. Any comments on this situation? Thanks!
mellowfin mellowfin
Hi , can you please attach your existing logo . Thanks

```html
<!DOCTYPE html>
<html lang="en">
<head>
<meta charset="utf-8">
<title>VEXA-Fjord ehf. Stationery</title>
<link rel="stylesheet" href="https://fonts.googleapis.com/css2?family=Open+Sans:wght@400;600;700&display=swap">
<style>
  :root{
    --bg:#eef0f2;
    --paper:#ffffff;
    --edge:#dde1e5;
    --blue:#1c6cc0;
    --blue-light:#4ba6e4;
    --blue-dark:#134f94;
    --orange:#f39a1e;
    --ink:#4a4f55;
    --ink-soft:#8a9098;
  }
  *{margin:0;padding:0;box-sizing:border-box}
  html,body{width:1200px;height:936px;overflow:hidden;background:var(--bg);font-family:"Open Sans",Arial,sans-serif;color:var(--ink)}
  .canvas{position:relative;width:1200px;height:936px}
  .sheet{position:absolute;background:var(--paper);border:1px solid var(--edge);overflow:hidden;box-shadow:0 1px 3px rgba(0,0,0,.08)}

  .brand{display:flex;align-items:center;gap:6px}
  .brand-dot{border-radius:50%;background:var(--blue);flex:none}
  .brand-name{font-weight:700;color:var(--blue);white-space:nowrap}

  .band{position:absolute;left:0;bottom:0;width:100%;display:block}
  .web{position:absolute;font-size:6px;letter-spacing:2px;color:var(--ink-soft);white-space:nowrap}

  /* letterhead */
  .letterhead{left:172px;top:74px;width:400px;height:540px}
  .letterhead .brand{position:absolute;left:14px;top:10px}
  .letterhead .brand-dot{width:34px;height:34px}
  .letterhead .brand-name{font-size:12px}
  .contact{position:absolute;left:290px;top:14px;font-size:5.5px;line-height:9px}
  .contact li{list-style:none;display:flex;align-items:center;gap:4px;white-space:nowrap}
  .contact i{display:inline-block;width:5px;height:5px;border-radius:50%;background:var(--blue);flex:none}
  .letter{position:absolute;left:28px;right:60px;top:158px;font-size:5.2px;line-height:8px}
  .letter p{margin-bottom:8px}
  .letter .sign{margin-top:14px}
  .letter .sign strong{display:block;font-weight:600}

  /* folder */
  .folder{left:635px;top:74px;width:423px;height:540px}
  .folder .brand{position:absolute;left:50%;top:228px;transform:translateX(-50%);gap:10px}
  .folder .brand-dot{width:44px;height:44px}
  .folder .brand-name{font-size:28px}

  /* business cards */
  .card{left:40px;width:208px;height:92px}
  .card-front{top:664px}
  .card-back{top:774px;height:84px;border:none;background:linear-gradient(135deg,var(--blue-light),var(--blue) 60%,var(--blue-dark))}
  .card-front .brand{position:absolute;left:8px;top:10px;gap:4px}
  .card-front .brand-dot{width:22px;height:22px}
  .card-front .brand-name{font-size:7px}
  .card-front .who{position:absolute;left:104px;top:10px;font-size:4.5px;line-height:6.5px;white-space:nowrap}
  .card-front .who strong{font-weight:700;display:block;font-size:5px}
  .card-back .brand{position:absolute;left:14px;top:27px;gap:6px}
  .card-back .brand-dot{width:30px;height:30px;background:var(--paper)}
  .card-back .brand-name{font-size:11px;color:var(--paper)}

  /* envelopes */
  .env-front{left:262px;top:668px;width:462px;height:188px}
  .env-front .brand{position:absolute;left:10px;top:10px;gap:5px}
  .env-front .brand-dot{width:34px;height:34px}
  .env-front .brand-name{font-size:10px}
  .env-front .return{position:absolute;left:62px;top:96px;font-size:6px;line-height:9px}
  .env-back{left:740px;top:672px;width:428px;height:182px}
  .env-back .flap{position:absolute;left:0;top:0;width:100%;height:100%}
  .env-back .web{left:50%;top:20px;transform:translateX(-50%);color:var(--paper);font-size:6.5px;letter-spacing:3px}
</style>
</head>
<body>
<main class="canvas">

  <section class="sheet letterhead">
    <div class="brand"><span class="brand-dot"></span><span class="brand-name">VEXA-Fjord</span></div>
    <ul class="contact">
      <li><i></i>Hvalsteinsgata 17</li>
      <li><i></i>108 Reykjavik Iceland</li>
      <li><i></i>+354 555 0142</li>
      <li><i></i>info@vexafjord.is</li>
    </ul>
    <div class="letter">
      <p>July 1, 2014</p>
      <p><strong>Dear Sirs,</strong><br>Hvalsteinsgata 17, 108 Reykjavik Iceland</p>
      <p>Thank you for your interest in our catch. Every order we ship is landed from cold northern waters by small boats and packed the same day. We take pride in fresh, honest seafood and in long partnerships with the kitchens we serve.</p>
      <p>Our season plan for the coming year is attached for your review. It lists expected volumes of cod, haddock and langoustine, with delivery windows for each port. Please let us know which items suit your menu so we can reserve stock early.</p>
      <p>We look forward to working with you and welcome any questions about sourcing, handling or prices.</p>
      <p>Best Regards,</p>
      <p class="sign"><strong>Einar Sólberg</strong>President<br>Hvalsteinsgata 17, 108 Reykjavik</p>
    </div>
    <span class="web" style="left:28px;bottom:14px">www.vexafjord.is</span>
    <svg class="band" height="7" viewBox="0 0 400 7" preserveAspectRatio="none">
      <rect width="400" height="7" fill="var(--blue)"/>
      <polygon points="240,0 400,0 400,7 232,7" fill="var(--orange)"/>
    </svg>
  </section>

  <section class="sheet folder">
    <div class="brand"><span class="brand-dot"></span><span class="brand-name">VEXA-Fjord</span></div>
    <span class="web" style="left:10px;bottom:14px">www.vexafjord.is</span>
    <svg class="band" height="7" viewBox="0 0 423 7" preserveAspectRatio="none">
      <rect width="423" height="7" fill="var(--blue)"/>
      <polygon points="255,0 423,0 423,7 247,7" fill="var(--orange)"/>
    </svg>
  </section>

  <section class="sheet card card-front">
    <div class="brand"><span class="brand-dot"></span><span class="brand-name">VEXA-Fjord</span></div>
    <div class="who">
      <strong>Einar Sólberg</strong>President<br>
      +354 555 0142<br>info@vexafjord.is<br>Hvalsteinsgata 17<br>108 Reykjavik Iceland
    </div>
    <svg class="band" height="6" viewBox="0 0 208 6" preserveAspectRatio="none">
      <rect width="208" height="6" fill="var(--blue)"/>
      <polygon points="110,0 208,0 208,6 104,6" fill="var(--orange)"/>
    </svg>
  </section>

  <section class="sheet card card-back">
    <div class="brand"><span class="brand-dot"></span><span class="brand-name">VEXA-Fjord</span></div>
  </section>

  <section class="sheet env-front">
    <div class="brand"><span class="brand-dot"></span><span class="brand-name">VEXA-Fjord</span></div>
    <div class="return">Hvalsteinsgata 17 108 Reykjavik Iceland</div>
    <span class="web" style="left:50%;bottom:14px;transform:translateX(-50%)">www.vexafjord.is</span>
    <svg class="band" height="6" viewBox="0 0 462 6" preserveAspectRatio="none">
      <rect width="462" height="6" fill="var(--blue)"/>
      <polygon points="290,0 462,0 462,6 282,6" fill="var(--orange)"/>
    </svg>
  </section>

  <section class="sheet env-back">
    <svg class="flap" viewBox="0 0 428 182" preserveAspectRatio="none">
      <defs>
        <linearGradient id="flapFill" x1="0" y1="0" x2="0" y2="1">
          <stop offset="0" stop-color="var(--blue-light)"/>
          <stop offset="1" stop-color="var(--blue)"/>
        </linearGradient>
      </defs>
      <polygon points="0,0 428,0 428,36 214,80 0,36" fill="url(#flapFill)"/>
      <polygon points="0,36 214,80 428,36 428,42 214,86 0,42" fill="var(--blue-dark)" opacity=".3"/>
    </svg>
    <span class="web">www.vexafjord.is</span>
  </section>

</main>
</body>
</html>
```